Bright Ridge Plumbing is a family owned plumbing company on Sydney's Northern Beaches. We are looking for a catchy business card that will appeal to consumes and stick in peoples minds. Our colours are Yellow Aqua and Blues.

The design should be something that will remind the consume we are the people the call with any plumbing needs.

Target Market(s)

property owners and managers.

Industry/Entity Type

Business

Contact Information for Business Card

Bright Ridge Plumbing, Martin Gowry, 0417 338 264, Admin@brightridgeplumbing.example, www.brightridgeplumbing.example, Plumber

```html
<!DOCTYPE html>
<html lang="en">
<head>
<meta charset="utf-8">
<title>Bright Ridge Plumbing – Business Card</title>
<link rel="stylesheet" href="https://fonts.googleapis.com/css2?family=Archivo:wght@600;800&family=Montserrat:wght@400;500&display=swap">
<style>
  :root {
    --page-bg: #e6e9ec;
    --card-top: #f4f7f0;
    --card-mist: #dcecf1;
    --pale-yellow: #eef2b8;
    --band-yellow: #e3ea7c;
    --band-aqua: #5cc3dc;
    --band-blue: #2f9fd0;
    --band-teal: #3aa78f;
    --navy: #1e2f5c;
    --ink: #1f1f24;
    --rule-blue: #2a5fa8;
    --icon-blue: #2f4f8f;
  }
  * { box-sizing: border-box; margin: 0; padding: 0; }
  html, body {
    width: 1200px; height: 960px; overflow: hidden;
    background: var(--page-bg);
  }
  .card {
    position: absolute;
    left: 100px; top: 194px;
    width: 1000px; height: 572px;
    overflow: hidden;
    box-shadow: 0 18px 40px rgba(30, 40, 60, 0.25);
    background:
      linear-gradient(90deg, rgba(255,255,255,0.25) 0 2%, rgba(255,255,255,0) 2% 6%, rgba(255,255,255,0.2) 6% 7%, rgba(255,255,255,0) 7% 18%, rgba(255,255,255,0.22) 18% 20%, rgba(255,255,255,0) 20% 44%, rgba(255,255,255,0.2) 44% 46%, rgba(255,255,255,0) 46% 100%),
      linear-gradient(180deg,
        var(--card-top) 0%,
        var(--card-mist) 38%,
        #e6f0e6 58%,
        var(--pale-yellow) 64%,
        var(--band-yellow) 69%,
        #bfe2c9 72%,
        var(--band-aqua) 77%,
        var(--band-blue) 84%,
        var(--band-aqua) 90%,
        var(--band-teal) 100%);
  }
  .card__rule {
    position: absolute;
    left: 118px; top: 30px;
    width: 3px; height: 408px;
    background: var(--rule-blue);
  }
  .brand {
    position: absolute;
    right: 90px; top: 120px;
    text-align: right;
    font-family: "Archivo", sans-serif;
    color: var(--navy);
  }
  .brand__line {
    display: flex; align-items: center; gap: 14px; justify-content: flex-end;
  }
  .brand__name {
    font-weight: 800;
    font-size: 40px;
    letter-spacing: 0.5px;
    text-transform: uppercase;
  }
  .brand__dot {
    width: 30px; height: 30px; border-radius: 50%;
    background: var(--band-aqua);
  }
  .brand__tagline {
    margin-top: 4px; margin-right: 44px;
    font-weight: 600;
    font-size: 23px;
    text-transform: uppercase;
  }
  .holder {
    position: absolute;
    left: 146px; top: 318px;
    display: flex; align-items: center; gap: 14px;
  }
  .holder__bar {
    width: 11px; height: 48px;
    background: var(--rule-blue);
  }
  .holder__name {
    font-family: "Archivo", sans-serif;
    font-weight: 800;
    font-size: 40px;
    color: var(--ink);
    text-transform: uppercase;
    white-space: nowrap;
  }
  .contacts {
    position: absolute;
    left: 540px; top: 302px;
    list-style: none;
    font-family: "Montserrat", sans-serif;
    font-size: 20px;
    color: var(--ink);
  }
  .contacts li {
    display: flex; align-items: center; gap: 14px;
    height: 34px;
    white-space: nowrap;
  }
  .contacts svg { width: 22px; height: 22px; flex: none; }
</style>
</head>
<body>
  <section class="card" aria-label="Bright Ridge Plumbing business card">
    <div class="card__rule"></div>

    <div class="brand">
      <div class="brand__line">
        <span class="brand__name">Bright Ridge Plumbing</span>
        <span class="brand__dot"></span>
      </div>
      <div class="brand__tagline">Water Drainage &amp; Gas</div>
    </div>

    <div class="holder">
      <span class="holder__bar"></span>
      <h1 class="holder__name">Martin Gowry</h1>
    </div>

    <ul class="contacts">
      <li>
        <svg viewBox="0 0 24 24" aria-hidden="true"><rect x="7" y="2" width="10" height="20" rx="2" fill="none" stroke="var(--icon-blue)" stroke-width="1.6"/><line x1="10" y1="19" x2="14" y2="19" stroke="var(--icon-blue)" stroke-width="1.6"/></svg>
        <span>0417 338 264</span>
      </li>
      <li>
        <svg viewBox="0 0 24 24" aria-hidden="true"><rect x="2" y="5" width="20" height="14" fill="var(--icon-blue)"/><path d="M2 5 L12 13 L22 5" fill="none" stroke="#fff" stroke-width="1.6"/></svg>
        <span>Admin@brightridgeplumbing.example</span>
      </li>
      <li>
        <svg viewBox="0 0 24 24" aria-hidden="true"><rect x="4" y="5" width="16" height="11" fill="none" stroke="var(--icon-blue)" stroke-width="1.6"/><line x1="1" y1="19" x2="23" y2="19" stroke="var(--icon-blue)" stroke-width="2"/></svg>
        <span>www.brightridgeplumbing.example</span>
      </li>
    </ul>
  </section>
</body>
</html>
```